Marlowe Shopcraft Interiors web design

We need to relaunch my commercial and retail interior design + construction company after being out of the industry's for 10 plus years.

```html
<!DOCTYPE html>
<html lang="en">
<head>
<meta charset="utf-8">
<title>Marlowe Shopcraft Interiors</title>
<link href="https://fonts.googleapis.com/css2?family=Krona+One&family=Roboto:wght@400;500;700&display=swap" rel="stylesheet">
<style>
:root{
  --ink:#111;
  --muted:#333;
  --brand:#1f3a78;
  --brand-deep:#0c2a6a;
  --accent:#2f6fe6;
  --tag:#efefef;
  --white:#fff;
}
*{box-sizing:border-box;margin:0;padding:0}
html,body{width:1200px;height:5226px;overflow:hidden;background:var(--white)}
body{font-family:"Roboto",Arial,sans-serif;color:var(--ink)}
.page{position:relative;width:1200px;height:5226px;overflow:hidden}
.photo{position:absolute}

/* header */
.site-header{position:absolute;left:0;top:0;width:1200px;height:97px;background:var(--white);z-index:2}
.brand-box{position:absolute;left:71px;top:20px;width:162px;height:162px;background:var(--white);z-index:3;display:flex;align-items:center;justify-content:center;flex-direction:column;gap:8px;text-align:center}
.brand-box .mark{width:22px;height:22px;background:var(--accent)}
.brand-box .name{font-weight:700;font-size:16px;line-height:1.2;color:var(--accent);padding:0 12px}
.main-nav{position:absolute;top:41px;left:364px;display:flex;gap:30px}
.main-nav a,.footer-nav a{font-family:"Krona One",sans-serif;font-size:12px;color:var(--brand);text-decoration:none;letter-spacing:.3px;white-space:nowrap}
.btn-outline-pill{position:absolute;left:905px;top:33px;width:137px;height:32px;border:1.5px solid var(--brand);border-radius:16px;font-family:"Krona One",sans-serif;font-size:12px;color:var(--brand);display:flex;align-items:center;justify-content:center}
.signup{position:absolute;left:1066px;top:41px;font-family:"Krona One",sans-serif;font-size:12px;color:var(--brand)}

/* hero */
.hero{position:absolute;left:0;top:97px;width:1200px;height:657px;background:linear-gradient(160deg,#1f3222 0%,#3a4a2c 30%,#8a6434 55%,#a57a40 70%,#5a4a33 100%)}
.hero-title{position:absolute;left:83px;top:233px;font-family:"Krona One",sans-serif;font-weight:400;font-size:34px;line-height:54px;color:var(--white);letter-spacing:.5px;white-space:nowrap}
.hero-sub{position:absolute;left:83px;top:362px;font-family:"Krona One",sans-serif;font-size:11px;line-height:22px;color:var(--white);width:560px}
.hero-learn{position:absolute;left:83px;top:431px;width:116px;height:28px;border:1.5px solid var(--white);border-radius:14px;font-family:"Krona One",sans-serif;font-size:10px;color:var(--white);display:flex;align-items:center;justify-content:center}
.hero-contact{position:absolute;left:215px;top:439px;font-family:"Krona One",sans-serif;font-size:10px;color:var(--white)}

/* headings */
.section-title{position:absolute;left:0;width:1200px;text-align:center;font-weight:500;color:var(--ink)}
.eyebrow{position:absolute;left:0;width:1200px;text-align:center;font-size:12px;font-weight:700}
.lead{position:absolute;left:0;width:1200px;text-align:center;font-size:15px}

/* steps */
.step-title{position:absolute;width:338px;text-align:center;font-size:20px;font-weight:700}
.step-text{position:absolute;width:338px;text-align:center;font-size:13px;line-height:20px;padding:0 20px}
.link-more{position:absolute;display:flex;align-items:center;gap:10px;font-size:13px}
.link-more svg,.proj-btn svg{width:16px;height:16px}

/* projects */
.proj-title{position:absolute;font-size:19px;font-weight:700}
.proj-desc{position:absolute;font-size:13px;white-space:nowrap}
.tags{position:absolute;display:flex;gap:8px}
.tag{background:var(--tag);font-size:10.5px;font-weight:700;padding:4px 8px}
.proj-btn{position:absolute;display:flex;align-items:center;gap:10px;font-size:13px}
.btn-box{position:absolute;left:557px;top:3324px;width:88px;height:41px;border:2px solid #666;font-size:13px;display:flex;align-items:center;justify-content:center}

/* story */
.story-title{position:absolute;left:634px;top:3522px;width:540px;font-size:40px;line-height:48px;font-weight:700}
.story-copy{position:absolute;left:634px;top:3622px;width:520px;font-size:13px;line-height:19.5px;color:var(--muted)}
.story-copy p{margin-bottom:14px}

/* form */
.field-label{position:absolute;left:367px;font-size:13px}
.field{position:absolute;left:367px;width:466px;border:1.5px solid #555;font-size:13px;padding:0 10px;display:flex;align-items:center}
.field.area{align-items:flex-start;padding-top:12px}
.check{position:absolute;left:540px;top:4785px;display:flex;align-items:center;gap:6px;font-size:13px}
.check span{width:16px;height:16px;border:1.5px solid #555;display:block}
.btn-solid{position:absolute;left:559px;top:4834px;width:82px;height:39px;background:var(--brand-deep);color:var(--white);font-size:13px;display:flex;align-items:center;justify-content:center}

/* footer */
.footer-rail{position:absolute;left:0;top:4965px;width:2px;height:261px;background:#222}
.footer-logo{position:absolute;left:83px;top:5039px;font-size:22px;font-weight:700;color:var(--brand)}
.footer-nav{position:absolute;left:404px;top:5046px;display:flex;gap:30px}
.socials{position:absolute;left:973px;top:5043px;display:flex;gap:10px}
.socials span{width:16px;height:16px;border-radius:50%;background:var(--brand);display:block}
.footer-line{position:absolute;left:190px;top:5116px;width:899px;height:1px;background:#999}
.legal{position:absolute;left:274px;top:5168px;display:flex;gap:66px;font-size:10.5px}
.legal .links{display:flex;gap:20px}
.legal .links a{color:var(--brand);text-decoration:underline}
</style>
</head>
<body>
<div class="page">

  <header class="site-header">
    <nav class="main-nav">
      <a href="#">HOME</a><a href="#">HOW IT WORKS</a><a href="#">WORK</a><a href="#">ETHOS</a><a href="#">CONTACT</a>
    </nav>
    <div class="btn-outline-pill">GET STARTED</div>
    <div class="signup">SIGN UP</div>
  </header>
  <div class="brand-box"><span class="mark"></span><span class="name">Marlowe Shopcraft Interiors</span></div>

  <section class="hero" role="img" aria-label="Timber-framed building under construction surrounded by forest">
    <h1 class="hero-title">DESIGNING BOLD, DURABLE,<br>AND INVITING RETAIL SPACES</h1>
    <p class="hero-sub">WATCH OUR FOUNDER EXPLAIN HOW WE PLAN, BUILD AND FIT OUT STORES, OFFICES AND SHOWROOMS.</p>
    <div class="hero-learn">LEARN MORE</div>
    <div class="hero-contact">CONTACT</div>
  </section>

  <!-- gallery strip -->
  <div class="photo" style="left:0;top:772px;width:71px;height:280px;background:linear-gradient(#8a5a3a,#b5552c,#5a6a5a)" role="img" aria-label="Autumn trees by a lake"></div>
  <div class="photo" style="left:83px;top:772px;width:345px;height:280px;background:linear-gradient(#c9c2d3,#e9d8cf 45%,#3a3b3e 80%,#6a6f78)" role="img" aria-label="Black pavilion on a rocky lakeshore at dusk"></div>
  <div class="photo" style="left:442px;top:772px;width:344px;height:280px;background:linear-gradient(#b9bec5,#a5613c 40%,#3a3430 60%,#8b8f94)" role="img" aria-label="Dark building reflected in a lake among autumn trees"></div>
  <div class="photo" style="left:801px;top:772px;width:344px;height:280px;background:linear-gradient(#a9b2b6,#7e8578 40%,#2b3326 70%,#424a36)" role="img" aria-label="Black building in the forest below a mountain"></div>
  <div class="photo" style="left:1157px;top:772px;width:43px;height:280px;background:linear-gradient(#9a3a20,#c25a2c,#6a3a20)" role="img" aria-label="Red autumn foliage"></div>
  <div class="photo" style="left:0;top:1068px;width:243px;height:79px;background:linear-gradient(90deg,#d8d2cc,#b5502a 40%,#c9c6c1)" role="img" aria-label="Autumn treeline"></div>
  <div class="photo" style="left:257px;top:1068px;width:345px;height:79px;background:linear-gradient(90deg,#8d9a8f,#c4cbc4,#7c8a80)" role="img" aria-label="Misty green hillside"></div>
  <div class="photo" style="left:616px;top:1068px;width:345px;height:79px;background:linear-gradient(90deg,#e3e1df,#d5d0cc 40%,#b8502a 75%,#c98a5a)" role="img" aria-label="Autumn trees under a pale sky"></div>
  <div class="photo" style="left:975px;top:1068px;width:225px;height:79px;background:linear-gradient(90deg,#b5482a,#e6e4e1 50%,#bcc4c0)" role="img" aria-label="Autumn foliage and distant pines"></div>

  <!-- how it works -->
  <h2 class="section-title" style="top:1262px;font-size:30px">How it Works</h2>

  <div class="photo" style="left:53px;top:1368px;width:338px;height:199px;background:linear-gradient(135deg,#c9c3b6,#6d5f4f 50%,#e0d4bc)" role="img" aria-label="Builders handling timber on site"></div>
  <div class="photo" style="left:430px;top:1368px;width:338px;height:199px;background:linear-gradient(135deg,#3a3a36,#d2b58a 40%,#efe9dd 60%,#2f2d2a)" role="img" aria-label="Builders reviewing construction plans"></div>
  <div class="photo" style="left:809px;top:1368px;width:338px;height:199px;background:linear-gradient(#d9dfe3,#3f5a3a 45%,#c9a56d 80%,#9a8a6a)" role="img" aria-label="Building frame on a timber base in the woods"></div>

  <h3 class="step-title" style="left:53px;top:1595px">Design &amp; Planning</h3>
  <h3 class="step-title" style="left:430px;top:1595px">Build &amp; Fit-Out</h3>
  <h3 class="step-title" style="left:809px;top:1595px">Final Inspection</h3>
  <p class="step-text" style="left:53px;top:1636px">We map your floor plan, brand and budget into a store layout that drives sales.</p>
  <p class="step-text" style="left:430px;top:1636px">Our crews build joinery, lighting and fixtures on schedule with minimal downtime.</p>
  <p class="step-text" style="left:809px;top:1636px">Before handing over the keys, we check every finish so you can open with confidence.</p>
  <div class="link-more" style="left:175px;top:1702px">Learn More <svg viewBox="0 0 16 16"><circle cx="8" cy="8" r="8" fill="#111"/><path d="M6 4.5 9.5 8 6 11.5" stroke="#fff" stroke-width="2" fill="none"/></svg></div>
  <div class="link-more" style="left:553px;top:1702px">Learn More <svg viewBox="0 0 16 16"><circle cx="8" cy="8" r="8" fill="#111"/><path d="M6 4.5 9.5 8 6 11.5" stroke="#fff" stroke-width="2" fill="none"/></svg></div>
  <div class="link-more" style="left:930px;top:1702px">Learn More <svg viewBox="0 0 16 16"><circle cx="8" cy="8" r="8" fill="#111"/><path d="M6 4.5 9.5 8 6 11.5" stroke="#fff" stroke-width="2" fill="none"/></svg></div>

  <!-- work -->
  <div class="eyebrow" style="top:1906px">Projects</div>
  <h2 class="section-title" style="top:1938px;font-size:36px">Work</h2>
  <p class="lead" style="top:2008px">Browse our retail, hospitality and office interior projects</p>

  <div class="photo" style="left:55px;top:2096px;width:525px;height:294px;background:linear-gradient(#8ea1ad,#3a4a35 40%,#c9d6e0 60%,#5a6a3a)" role="img" aria-label="Light-clad building and red barn at dusk"></div>
  <h3 class="proj-title" style="left:55px;top:2412px">Boutique Storefront</h3>
  <p class="proj-desc" style="left:55px;top:2447px">Full refit of a fashion boutique with custom shelving and feature lighting</p>
  <div class="tags" style="left:55px;top:2480px"><span class="tag">Retail</span><span class="tag">Renovation</span><span class="tag">Joinery</span></div>
  <div class="proj-btn" style="left:72px;top:2523px">Button <svg viewBox="0 0 16 16"><circle cx="8" cy="8" r="8" fill="#111"/><path d="M6 4.5 9.5 8 6 11.5" stroke="#fff" stroke-width="2" fill="none"/></svg></div>

  <div class="photo" style="left:55px;top:2597px;width:525px;height:294px;background:linear-gradient(135deg,#e6e4dc,#6c8a4a 40%,#8a5a34 70%,#3a3330)" role="img" aria-label="Lounge with leather sofas and large windows"></div>
  <h3 class="proj-title" style="left:55px;top:2913px">Client Lounge Fit-Out</h3>
  <p class="proj-desc" style="left:55px;top:2947px">Turned an empty office floor into a warm and flexible client lounge</p>
  <div class="tags" style="left:55px;top:2981px"><span class="tag">Office</span><span class="tag">Lounge</span><span class="tag">Fit-out</span></div>
  <div class="proj-btn" style="left:72px;top:3023px">Button <svg viewBox="0 0 16 16"><circle cx="8" cy="8" r="8" fill="#111"/><path d="M6 4.5 9.5 8 6 11.5" stroke="#fff" stroke-width="2" fill="none"/></svg></div>

  <div class="photo" style="left:618px;top:2096px;width:527px;height:523px;background:linear-gradient(#c8d0d3,#4a6a38 35%,#e8e6e0 55%,#5b7a2e 75%,#466a24)" role="img" aria-label="White modern building in a grassy forest clearing"></div>
  <h3 class="proj-title" style="left:618px;top:2641px">Flagship Showroom</h3>
  <p class="proj-desc" style="left:618px;top:2676px">New-build showroom shell and interior fit-out with energy-efficient lighting</p>
  <div class="tags" style="left:618px;top:2709px"><span class="tag">Showroom</span><span class="tag">New build</span><span class="tag">Energy efficient</span></div>
  <div class="proj-btn" style="left:635px;top:2752px">Button <svg viewBox="0 0 16 16"><circle cx="8" cy="8" r="8" fill="#111"/><path d="M6 4.5 9.5 8 6 11.5" stroke="#fff" stroke-width="2" fill="none"/></svg></div>

  <div class="photo" style="left:618px;top:2826px;width:527px;height:294px;background:linear-gradient(135deg,#c08a4a,#e2b77a 40%,#9ab58a 55%,#b27a3a)" role="img" aria-label="Timber-lined dining room with table and chairs"></div>
  <h3 class="proj-title" style="left:618px;top:3142px">Café Interior Refit</h3>
  <p class="proj-desc" style="left:618px;top:3176px">Timber-lined café with bespoke counters, seating and a bright glazed wall</p>
  <div class="tags" style="left:618px;top:3210px"><span class="tag">Hospitality</span><span class="tag">Renovation</span><span class="tag">Timber</span></div>
  <div class="proj-btn" style="left:635px;top:3253px">Button <svg viewBox="0 0 16 16"><circle cx="8" cy="8" r="8" fill="#111"/><path d="M6 4.5 9.5 8 6 11.5" stroke="#fff" stroke-width="2" fill="none"/></svg></div>

  <div class="btn-box">Button</div>

  <!-- story -->
  <div class="photo" style="left:53px;top:3507px;width:515px;height:531px;background:linear-gradient(#c8d0d3,#4a6a38 35%,#e8e6e0 55%,#5b7a2e 75%,#466a24)" role="img" aria-label="White modern building in a grassy forest clearing"></div>
  <h2 class="story-title">Creating Commercial Spaces That Sell</h2>
  <div class="story-copy">
    <p>For more than two decades our team has designed and built interiors for shops, cafés, offices and showrooms. We handle everything from the first sketch to the last fixture, so owners deal with one trusted partner from start to opening day.</p>
    <p>Every project begins with how your customers move, browse and buy. We plan layouts, lighting and display joinery around your brand, then build them with our own carpenters, shopfitters and project managers on site.</p>
    <p>Now back in the industry with fresh ideas and proven craft, we work closely with retailers and landlords to deliver fit-outs on time and on budget. Durable materials, clean detailing and careful scheduling keep your doors open and your space working hard for years to come.</p>
  </div>

  <!-- contact -->
  <div class="eyebrow" style="top:4227px">Get Started</div>
  <h2 class="section-title" style="top:4259px;font-size:36px">Contact Now</h2>
  <p class="lead" style="top:4329px">Ready to start your next store or office fit-out? Contact us today!</p>
  <div class="field-label" style="top:4417px">Name</div>
  <div class="field" style="top:4441px;height:41px">Placeholder</div>
  <div class="field-label" style="top:4504px">Email</div>
  <div class="field" style="top:4529px;height:40px">Placeholder</div>
  <div class="field-label" style="top:4591px">Message</div>
  <div class="field area" style="top:4613px;height:150px">Enter your message...</div>
  <div class="check"><span></span>Checkbox</div>
  <div class="btn-solid">Button</div>

  <!-- footer -->
  <div class="footer-rail"></div>
  <div class="footer-logo">Logo</div>
  <nav class="footer-nav"><a href="#">HOME</a><a href="#">HOW IT WORKS</a><a href="#">WORK</a><a href="#">ETHOS</a><a href="#">CONTACT</a></nav>
  <div class="socials" aria-label="Social links"><span></span><span></span><span></span><span></span><span></span></div>
  <div class="footer-line"></div>
  <div class="legal"><span>© 2023 Logo. All rights reserved.</span><span class="links"><a href="#">Privacy Policy</a><a href="#">Terms and Conditions</a><a href="#">Cookie Policy</a></span></div>

</div>
</body>
</html>
```